Business Card Design

I do estate sales and would like business card to reflect look and feel of attached logo. I also have copy of logo in .eps and .tif if you need that instead of .jpeg.
Updates

sorry for the delay in reviewing these designs. I will pick one by tomorrow. Here are the absolutes: *must have tagline (we find good homes for your treasures *must use blue and green *must be horizontal *nothing too fancy please submit your best and final. Thanks so much!

Industry/Entity Type

Business

Contact Information for Business Card

Nora Platt

DEALS by NORA
We find good homes for your treasures.

Specializing in one to three-day sales
o (no sale too big or too small)
• Home and garage organizing
• Home Clean-out

Call Nora Platt at 202-555-0187
to schedule.

```html
<!DOCTYPE html>
<html lang="en">
<head>
<meta charset="utf-8">
<title>DEALS by NORA – Business Card</title>
<link rel="stylesheet" href="https://fonts.googleapis.com/css2?family=Arimo:wght@400;700&display=swap">
<style>
  :root {
    --page-bg: #ece8e1;
    --card-grey: #e4e6e6;
    --photo-light: #eef0ef;
    --photo-mid: #c9cecc;
    --band-blue: #272b7a;
    --navy-text: #262a72;
    --name-green: #3fb94a;
    --logo-green: #6b8a3a;
    --white: #ffffff;
  }
  * { margin: 0; padding: 0; box-sizing: border-box; }
  html, body {
    width: 1200px; height: 900px; overflow: hidden;
    background: var(--page-bg);
    font-family: "Arimo", Arial, sans-serif;
  }
  .card {
    position: absolute; left: 75px; top: 150px;
    width: 1050px; height: 600px;
    background: var(--card-grey);
    overflow: hidden;
  }
  .card-art { position: absolute; inset: 0; }
  .contact { position: absolute; right: 110px; top: 48px; text-align: left; }
  .contact-name {
    color: var(--name-green); font-size: 40px; font-weight: 400;
    margin-left: 60px; letter-spacing: -0.5px;
  }
  .contact-phone {
    display: flex; align-items: center; gap: 12px;
    color: var(--navy-text); font-size: 46px; font-weight: 700;
    letter-spacing: -1px; margin-top: 6px;
  }
  .contact-phone svg { width: 40px; height: 32px; }
  .services {
    position: absolute; left: 620px; top: 200px;
    list-style: none; color: var(--white); font-size: 29px;
  }
  .services li { margin-bottom: 8px; }
  .services li::before {
    content: ""; display: inline-block; width: 11px; height: 11px;
    border-radius: 50%; background: var(--white);
    margin-right: 12px; vertical-align: middle;
  }
  .brand-name {
    position: absolute; left: 80px; top: 225px;
    color: var(--logo-green); font-size: 60px; font-weight: 400;
    line-height: 1.05; text-align: center; letter-spacing: 2px;
  }
  .tagline {
    position: absolute; left: 290px; top: 520px;
    color: var(--navy-text); font-size: 21px; font-weight: 700;
    white-space: nowrap;
    transform-origin: left center; transform: rotate(-16deg);
  }
</style>
</head>
<body>
  <div class="card">
    <svg class="card-art" viewBox="0 0 1050 600" width="1050" height="600">
      <defs>
        <linearGradient id="houseTone" x1="0" y1="0" x2="0" y2="1">
          <stop offset="0" stop-color="var(--photo-light)"/>
          <stop offset="0.5" stop-color="var(--photo-mid)"/>
          <stop offset="1" stop-color="var(--photo-light)"/>
        </linearGradient>
      </defs>
      <rect class="house-photo" role="img" aria-label="Faded photo of a house with a front lawn"
            x="0" y="0" width="1050" height="600" fill="url(#houseTone)"/>
      <path class="blue-band" fill="var(--band-blue)"
            d="M0,15 C300,165 700,175 1050,120 L1050,275 C800,330 420,420 120,600 L0,600 Z"/>
    </svg>

    <div class="contact">
      <div class="contact-name">Nora Platt</div>
      <div class="contact-phone">
        <svg viewBox="0 0 40 32" aria-hidden="true">
          <path fill="var(--navy-text)" d="M2,10 C2,4 38,4 38,10 L38,13 L29,13 L29,9 L11,9 L11,13 L2,13 Z"/>
          <path fill="var(--navy-text)" d="M8,14 L14,14 L14,11 L26,11 L26,14 L32,14 L36,30 L4,30 Z"/>
          <circle cx="20" cy="21" r="4" fill="var(--card-grey)"/>
        </svg>
        <span>202-555-0187</span>
      </div>
    </div>

    <ul class="services">
      <li>Home and garage organizing</li>
      <li>Home Clean-out</li>
    </ul>

    <div class="brand-name">DEALS<br>by<br>NORA</div>

    <p class="tagline">We find good homes for your treasures. Specializing in one to three-day sales</p>
  </div>
</body>
</html>
```